Private Chef booking platform landing page design

I need an amazing design for a landing page for my upcoming private chef booking platform Platerva. You can view my current page here: www.platerva.co.uk/mainindex.php. The design on this page is wrong right now. This platform is in Beta and the main purpose is to sign up chefs. Similar to what Rydexa.com is doing with their website -> become a driver. In my case we should have a button that says "become a chef", state the benefits of becoming a chef such as earning extra money, managing your time and bookings, increasing your client base and be creative with your food menus at the same time. Also, somewhere on the website it needs to say that we are currently in Beta mode and sign up to help us grow. In terms of visuals, I want the design to be sleek and clean and also adaptable to mobile devices as I am using html5. You can also re-design the current logo and choose any colours you think would be suitable for such a concept. Similar concept websites: hobwanderly.com and stovlin.com
Updates

Target Market(s)

upper middle class

Industry/Entity Type

Chef

Number of Pages Required

1 page

Font styles to use
Sans Serif

Requirements
Must have
• see brief and check hobwanderly.com and stovlin.com for inspiration and also rydexa.com
Nice to have
• see brief
Should not have
• bad visuals

```html
<!DOCTYPE html>
<html lang="en">
<head>
<meta charset="utf-8">
<title>Platerva – Private Chef Booking</title>
<link href="https://fonts.googleapis.com/css2?family=Oswald:wght@300;400&family=Open+Sans:wght@400;600&display=swap" rel="stylesheet">
<style>
:root{
  --ink:#222;
  --text:#555;
  --muted:#888;
  --white:#fff;
  --blue:#3d8fe8;
  --blue-band:#3b8de6;
  --nav-active:#1e1e1e;
  --footer-bg:#f2f2f2;
  --copy-bg:#e4e4e4;
  --line:#ddd;
}
*{box-sizing:border-box;margin:0;padding:0}
html,body{width:1200px;height:2200px;overflow:hidden}
body{font-family:"Open Sans",Arial,sans-serif;color:var(--text);background:var(--white)}
h1,h2,h3,.btn,.nav a,.beta-band p{font-family:"Oswald",Arial,sans-serif;font-weight:400}

/* header */
.site-header{height:100px;display:flex;justify-content:space-between;align-items:flex-start;padding:0 190px 0 190px;background:var(--white)}
.brand{display:flex;align-items:center;gap:10px;margin-top:22px}
.brand-mark{width:44px;height:44px;border-radius:50%;border:2px solid var(--ink)}
.brand-name{font-family:"Oswald",Arial,sans-serif;font-size:24px;color:var(--ink)}
.nav{display:flex;height:100px}
.nav a{display:flex;align-items:center;padding:0 16px;font-size:15px;color:var(--ink);text-decoration:none;text-transform:uppercase}
.nav a.active{background:var(--nav-active);color:var(--white)}

/* hero */
.hero{position:relative;height:390px;background:linear-gradient(135deg,#6a4a33 0%,#a0663d 35%,#d9c7b0 55%,#4b3b2e 80%,#2a2420 100%)}
.hero-title{position:absolute;left:300px;top:150px;width:600px;height:90px;background:rgba(30,25,20,.55);display:flex;align-items:center;justify-content:center}
.hero-title h1{font-size:38px;color:var(--white);text-transform:uppercase;letter-spacing:.5px}

/* welcome */
.welcome{height:650px;padding-top:48px;text-align:center}
.welcome h2{font-size:34px;color:var(--ink);text-transform:uppercase}
.welcome .intro{width:810px;margin:26px auto 0;font-size:12px;line-height:1.6;text-align:left}
.audience{display:flex;justify-content:center;gap:70px;margin-top:54px}
.audience-card{width:300px;text-align:left}
.audience-card h3{font-size:24px;color:var(--ink);text-align:center;text-transform:uppercase;margin-bottom:18px}
.audience-photo{height:140px}
.photo-cooking{background:linear-gradient(120deg,#8a6b4d,#c9b39a 50%,#5c7a3c)}
.photo-chef{background:linear-gradient(120deg,#3a2f28,#8d7c6c 50%,#e8e4df 60%,#2f2925)}
.audience-card p{font-size:11px;line-height:1.6;margin-top:14px}
.btn-row{display:flex;justify-content:center;gap:30px;margin-top:26px}
.btn{display:inline-flex;align-items:center;justify-content:center;text-transform:uppercase;text-decoration:none}
.btn-outline{width:112px;height:32px;border:1px solid var(--blue);color:var(--blue);font-size:13px}

/* testimonials + follow */
.showcase{position:relative;height:650px;background:linear-gradient(160deg,#2b231d 0%,#5a4530 35%,#3b3024 60%,#1d1915 100%);color:var(--white);text-align:center}
.showcase h2{font-size:28px;text-transform:uppercase;padding-top:34px}
.testimonial{position:relative;width:800px;margin:28px auto 0}
.testimonial p{font-size:13px;line-height:1.7}
.quote{position:absolute;font-family:"Oswald",Arial,sans-serif;font-size:70px;line-height:1;color:var(--white)}
.quote-open{left:-40px;top:-20px}
.quote-close{right:-40px;bottom:-30px}
.testimonial .author{margin-top:30px;font-size:13px}
.follow{margin-top:78px}
.follow h2{padding-top:0;font-size:36px}
.socials{display:flex;justify-content:center;gap:20px;margin-top:24px}
.social{width:64px;height:64px;border-radius:50%;border:2px solid var(--white)}
.cta-row{display:flex;justify-content:center;gap:26px;margin-top:42px}
.btn-solid{width:190px;height:54px;background:var(--blue);color:var(--white);font-size:16px}

/* beta band */
.beta-band{height:130px;background:var(--blue-band);display:flex;align-items:center;justify-content:center}
.beta-band p{font-size:24px;color:var(--white);text-transform:uppercase}

/* footer */
.site-footer{height:250px;background:var(--footer-bg);display:flex;padding:40px 0 0 190px;gap:0}
.footer-col{width:340px}
.footer-col h3{font-size:20px;color:var(--ink);text-transform:uppercase;margin-bottom:14px}
.footer-col li{list-style:none;font-size:12px;line-height:2.1;color:var(--text)}
.address li{display:flex;align-items:center;gap:10px}
.address svg{width:14px;height:14px;fill:var(--text)}
.copyright{height:30px;background:var(--copy-bg);display:flex;align-items:center;justify-content:center;font-size:11px;color:var(--muted)}
</style>
</head>
<body>

<header class="site-header">
  <div class="brand">
    <span class="brand-mark"></span>
    <span class="brand-name">Platerva</span>
  </div>
  <nav class="nav">
    <a class="active" href="#">Home</a>
    <a href="#">Contact Us</a>
    <a href="#">About Us</a>
    <a href="#">Sign Up</a>
    <a href="#">Login</a>
    <a href="#">Help</a>
  </nav>
</header>

<section class="hero" role="img" aria-label="Photo of a chef serving plated meals at a home dining table">
  <div class="hero-title"><h1>Chefs made meals in your home</h1></div>
</section>

<section class="welcome">
  <h2>Welcome to Platerva</h2>
  <p class="intro">Lorem ipsum dolor sit amet, consectetur adipiscing elit. Praesent at tincidunt tellus nec pulvinar nisl. Vivamus imperdiet ipsum lacus, eu suscipit lacus interdum sed. Donec a posuere magna. Vestibulum ante ipsum primis in faucibus orci luctus et ultrices posuere cubilia curae. Aliquam ac ipsum ut mi luctus bibendum at a erat. Nunc sodales felis tortor, at tincidunt tellus aliquet ut. Nulla congue sollicitudin suscipit. Fusce rutrum erat eget tellus tristique, vel facilisis justo volutpat. Curabitur ut mollis mi, ac fringilla felis.</p>
  <div class="audience">
    <article class="audience-card">
      <h3>I need a chef</h3>
      <div class="audience-photo photo-cooking" role="img" aria-label="Photo of hands chopping vegetables on a kitchen board"></div>
      <p>Lorem ipsum dolor sit amet, consectetur adipiscing elit. Praesent at tincidunt tellus nec pulvinar nisl. Vivamus imperdiet ipsum lacus, eu suscipit lacus interdum sed. Donec a posuere magna. Fusce rutrum erat eget tellus tristique, vel facilisis justo.</p>
      <div class="btn-row"><a class="btn btn-outline" href="#">Sign Up</a><a class="btn btn-outline" href="#">Log In</a></div>
    </article>
    <article class="audience-card">
      <h3>I am a chef</h3>
      <div class="audience-photo photo-chef" role="img" aria-label="Photo of a chef in whites standing in a professional kitchen"></div>
      <p>Lorem ipsum dolor sit amet, consectetur adipiscing elit. Praesent at tincidunt tellus nec pulvinar nisl. Vivamus imperdiet ipsum lacus, eu suscipit lacus interdum sed. Donec a posuere magna. Fusce rutrum erat eget tellus tristique, vel facilisis justo.</p>
      <div class="btn-row"><a class="btn btn-outline" href="#">Sign Up</a><a class="btn btn-outline" href="#">Log In</a></div>
    </article>
  </div>
</section>

<section class="showcase" role="img" aria-label="Dark background photo of a plated dish with potatoes and greens">
  <h2>Testimonials</h2>
  <blockquote class="testimonial">
    <span class="quote quote-open">“</span>
    <p>Lorem ipsum dolor sit amet, consectetur adipiscing elit. Vivamus sem leo, laoreet in posuere et, pellentesque nec, pharetra ut lectus. Nunc ullamcorper nisi nisl, vitae tincidunt lectus posuere vel. Donec feugiat ipsum vitae neque sodales blandit. Nunc aliquet elit ut velit consectetur vel aliquam. Nunc rhoncus, orci sed tincidunt malesuada.</p>
    <span class="quote quote-close">”</span>
    <p class="author">Mrs. Ana Lowe, Lorem Ipsum Co.</p>
  </blockquote>
  <div class="follow">
    <h2>Follow Us</h2>
    <div class="socials">
      <a class="social" href="#" aria-label="Social profile one"></a>
      <a class="social" href="#" aria-label="Social profile two"></a>
      <a class="social" href="#" aria-label="Social profile three"></a>
      <a class="social" href="#" aria-label="Social profile four"></a>
      <a class="social" href="#" aria-label="Social profile five"></a>
    </div>
    <div class="cta-row">
      <a class="btn btn-solid" href="#">Become a Chef</a>
      <a class="btn btn-solid" href="#">How it Works</a>
    </div>
  </div>
</section>

<section class="beta-band">
  <p>We are currently in beta mode and sign up to help us grow</p>
</section>

<footer>
  <div class="site-footer">
    <div class="footer-col">
      <h3>Benefits</h3>
      <ul>
        <li>Earn extra money</li>
        <li>Fully manage your bookings schedule</li>
        <li>Be creative with your food menus</li>
        <li>Expand your clientele base</li>
      </ul>
    </div>
    <div class="footer-col">
      <h3>Our Policy</h3>
      <ul>
        <li>Faq</li>
        <li>Blog</li>
        <li>Team</li>
        <li>Terms of Services</li>
      </ul>
    </div>
    <div class="footer-col address">
      <h3>Address</h3>
      <ul>
        <li><svg viewBox="0 0 24 24"><path d="M12 2a7 7 0 0 0-7 7c0 5 7 13 7 13s7-8 7-13a7 7 0 0 0-7-7zm0 9.5A2.5 2.5 0 1 1 12 6.5a2.5 2.5 0 0 1 0 5z"/></svg>London</li>
        <li><svg viewBox="0 0 24 24"><path d="M6.6 10.8a15 15 0 0 0 6.6 6.6l2.2-2.2a1 1 0 0 1 1-.25 11.4 11.4 0 0 0 3.6.57 1 1 0 0 1 1 1V20a1 1 0 0 1-1 1A17 17 0 0 1 3 4a1 1 0 0 1 1-1h3.5a1 1 0 0 1 1 1 11.4 11.4 0 0 0 .57 3.6 1 1 0 0 1-.25 1z"/></svg>020 7946 0112</li>
        <li><svg viewBox="0 0 24 24"><path d="M3 5h18v14H3zm2 2v.5l7 4.5 7-4.5V7l-7 4.5z"/></svg>chefs@platerva.co.uk</li>
      </ul>
    </div>
  </div>
  <div class="copyright">Copyright © 2014 Platerva. All Rights Reserved.</div>
</footer>

</body>
</html>
```